Varnath Consulting Business card design.

See our website www.varnathconsulting-example.com which will give you a good idea of what we are about. The font is called 'Play'.

I'd like a standout business card in keeping with the themes and branding on the website

Target Market(s)

professionals. HR directors

Industry/Entity Type

Business

Contact Information for Business Card

Varnath Consulting PO Box 3917 Tindale Creek NSW 2840 1300 457 318 Gerald Ashbury Principal email: jobs@varnathconsulting-example.com ABN: 31792048663

Font styles to use
Other font styles liked:
• Play

Requirements
Must have
• Must have same design colours and branding as website.
• On back I'd prefer a list of the things we do which appears below the name at the header on the website

```html
<!DOCTYPE html>
<html lang="en">
<head>
<meta charset="utf-8">
<title>Varnath Consulting – Business Card</title>
<link href="https://fonts.googleapis.com/css2?family=Open+Sans:wght@400;600;700&display=swap" rel="stylesheet">
<style>
  :root {
    --brand-red: #b01c1c;
    --text-grey: #5a5a5a;
    --mark-grey: #8c8c8c;
    --card-white: #ffffff;
    --backdrop: #ecebea;
  }
  html, body {
    margin: 0;
    padding: 0;
    width: 1200px;
    height: 900px;
    overflow: hidden;
    background: var(--backdrop);
    font-family: "Open Sans", Arial, sans-serif;
  }
  .canvas {
    position: relative;
    width: 1200px;
    height: 900px;
  }
  .card {
    position: absolute;
    background: var(--card-white);
    box-shadow: 0 4px 18px rgba(0,0,0,0.12);
    overflow: hidden;
  }
  .card--front { left: 238px; top: 62px; width: 555px; height: 343px; }
  .card--back  { left: 457px; top: 518px; width: 560px; height: 343px; }

  .front-wordmark {
    position: absolute;
    left: 26px;
    top: 70px;
    margin: 0;
    color: var(--brand-red);
    font-weight: 700;
    font-size: 48px;
    line-height: 1.05;
    letter-spacing: -0.5px;
  }

  .contact {
    position: absolute;
    left: 312px;
    top: 160px;
    color: var(--text-grey);
    font-size: 14px;
    line-height: 1.25;
    white-space: nowrap;
  }
  .contact p { margin: 0; }
  .contact__name {
    color: var(--brand-red);
    font-weight: 600;
    font-size: 17px;
  }
  .contact .contact__role { margin-bottom: 14px; }
  .contact .contact__abn { margin-bottom: 10px; }
  .contact__abn-label { color: var(--brand-red); font-weight: 700; }
  .contact .contact__row {
    display: flex;
    align-items: center;
    gap: 7px;
    margin-bottom: 3px;
  }
  .contact__row--email { font-size: 11.5px; }
  .contact__icon { width: 11px; height: 11px; flex: none; fill: var(--brand-red); }
  .contact .contact__address { margin-top: 4px; }

  .back-lockup {
    position: absolute;
    inset: 0;
    display: flex;
    align-items: center;
    justify-content: center;
    gap: 14px;
  }
  .back-lockup__dot {
    width: 14px;
    height: 14px;
    border-radius: 50%;
    background: var(--mark-grey);
  }
  .back-lockup__name {
    margin: 0;
    color: var(--brand-red);
    font-weight: 400;
    font-size: 38px;
    letter-spacing: 1px;
  }
</style>
</head>
<body>
<main class="canvas">

  <section class="card card--front" aria-label="Business card front">
    <p class="front-wordmark">Varnath<br>Consulting</p>

    <div class="contact">
      <p class="contact__name">Gerald Ashbury</p>
      <p class="contact__role">Principal</p>
      <p class="contact__abn"><span class="contact__abn-label">ABN:</span> 31792048663</p>
      <p class="contact__row">
        <svg class="contact__icon" viewBox="0 0 24 24" aria-hidden="true"><path d="M6.6 10.8a15.1 15.1 0 0 0 6.6 6.6l2.2-2.2a1 1 0 0 1 1-.25 11.4 11.4 0 0 0 3.6.57 1 1 0 0 1 1 1V20a1 1 0 0 1-1 1A17 17 0 0 1 3 4a1 1 0 0 1 1-1h3.5a1 1 0 0 1 1 1c0 1.25.2 2.45.57 3.6a1 1 0 0 1-.25 1z"/></svg>
        <span>1300 457 318</span>
      </p>
      <p class="contact__row contact__row--email">
        <svg class="contact__icon" viewBox="0 0 24 24" aria-hidden="true"><path d="M2 5h20v14H2z M2 5l10 8 10-8" stroke="#fff" stroke-width="1.6"/></svg>
        <span>jobs@varnathconsulting-example.com</span>
      </p>
      <p class="contact__address">PO Box 3917 Tindale<br>Creek NSW 2840</p>
    </div>
  </section>

  <section class="card card--back" aria-label="Business card back">
    <div class="back-lockup">
      <span class="back-lockup__dot" aria-hidden="true"></span>
      <p class="back-lockup__name">Varnath Consulting</p>
    </div>
  </section>

</main>
</body>
</html>
```